Brackenridge Strength Studio Chronic Pain Flyer

Double sided DL flyer required to promote a strength training studio to sufferers of chronic pain. Flyer will be displayed in osteopathy, chiropractic and massage clinics. Flyer should be clean, professional and appeal to an older (40+) demographic.

Target Market(s)

Chronic pain sufferers. Age 40+

Industry/Entity Type

Health And Wellness

Colors

Designer to choose colors to be used in the design.

Requirements
Must have
• See attached files for text copy and logo. Image(s) of people strength training with a coach or personal trainer, as well as images depicting pain in common parts of the body (such as those pictured in the supplied mock up)
• website address: brackenridgestrengthstudio.example.com.au
• phone number : 0452 918 304
• Street address: 4/63 Juniper Hollow Rd, Brackenridge
Nice to have
• Images such as in the attached files.

```html
<!DOCTYPE html>
<html lang="en">
<head>
<meta charset="utf-8">
<title>Brackenridge Strength Studio – Chronic Pain Flyer</title>
<link rel="stylesheet" href="https://fonts.googleapis.com/css2?family=Oswald:wght@300;400;500;700&family=Anton&display=swap">
<style>
  :root {
    --bg: #e4e4e4;
    --paper: #ffffff;
    --ink: #111111;
    --brand-red: #e03140;
    --deep-red: #c81f2e;
    --band-grey: #5d5f66;
    --logo-grey: #8a8c92;
    --photo-grey: #cfcfcf;
    --photo-shadow: #9d9d9d;
  }
  * { box-sizing: border-box; margin: 0; padding: 0; }
  html, body { width: 1200px; height: 1000px; overflow: hidden; }
  body {
    background: var(--bg);
    font-family: "Oswald", "Arial Narrow", sans-serif;
    position: relative;
  }
  .flyer {
    position: absolute;
    top: 60px;
    width: 420px;
    height: 880px;
    background: var(--paper);
    overflow: hidden;
    box-shadow: 0 6px 18px rgba(0,0,0,0.18);
  }
  .flyer--info { left: 150px; }
  .flyer--cover { left: 630px; }

  .brand-name {
    position: absolute;
    top: 44px; left: 0; width: 100%;
    text-align: center;
    font-weight: 700;
    font-size: 27px;
    line-height: 1;
    letter-spacing: 1px;
    text-transform: uppercase;
    color: var(--logo-grey);
  }
  .headline {
    position: absolute;
    top: 110px; left: 0; width: 100%;
    text-align: center;
    font-family: "Anton", "Oswald", sans-serif;
    text-transform: uppercase;
    line-height: 0.95;
  }
  .headline__lead { display: block; font-size: 36px; color: var(--ink); letter-spacing: 0.5px; }
  .headline__key { display: block; font-size: 66px; color: var(--brand-red); letter-spacing: 0.5px; }

  .copy {
    position: absolute;
    left: 40px; right: 40px;
    font-weight: 500;
    font-size: 15px;
    line-height: 1.35;
    color: var(--ink);
    text-align: justify;
    text-align-last: center;
  }
  .copy--intro { top: 248px; }
  .copy--offer { top: 478px; }
  .copy__cta { color: var(--deep-red); }

  .photo {
    position: absolute;
    background: radial-gradient(circle at 55% 55%, rgba(224,49,64,0.75) 0, rgba(224,49,64,0.25) 22%, transparent 40%),
                linear-gradient(160deg, var(--photo-grey), var(--photo-shadow));
  }
  .photo--knee { top: 345px; left: 128px; width: 165px; height: 118px; }
  .photo--back {
    top: 235px; left: 20px; width: 380px; height: 255px;
    background: radial-gradient(ellipse at 50% 78%, rgba(224,49,64,0.85) 0, rgba(224,49,64,0.35) 20%, transparent 38%),
                linear-gradient(180deg, #e9e9e9, var(--photo-shadow) 70%, #ffffff);
  }

  .base {
    position: absolute;
    left: 0; bottom: 0;
    width: 420px; height: 340px;
  }
  .flyer--cover .base { height: 370px; }

  .contact {
    position: absolute;
    left: 0; bottom: 70px; width: 100%;
    text-align: center;
    color: var(--paper);
  }
  .contact__phone { display: block; font-weight: 500; font-size: 50px; line-height: 1.1; letter-spacing: 1px; }
  .contact__web { display: block; font-weight: 500; font-size: 19px; line-height: 1.4; }
  .contact__address { display: block; font-weight: 300; font-size: 24px; line-height: 1.6; }
</style>
</head>
<body>

  <article class="flyer flyer--info">
    <div class="brand-name">Brackenridge Strength Studio</div>
    <h1 class="headline">
      <span class="headline__lead">Health Through</span>
      <span class="headline__key">Strength</span>
    </h1>
    <p class="copy copy--intro">Strength training has been shown to improve many chronic pain conditions and is now being routinely recommended by medical and health professionals</p>
    <div class="photo photo--knee" role="img" aria-label="Photo of hands holding a painful knee, highlighted in red"></div>
    <p class="copy copy--offer">Our private studio provides high quality strength training by expert strength coaches. We've helped countless people improve or eliminate chronic pain, <span class="copy__cta">contact us today and find out how we can help you.</span></p>
    <svg class="base" viewBox="0 0 420 340" preserveAspectRatio="none" aria-hidden="true">
      <path d="M0 0 Q 170 95 420 62 L420 340 L0 340 Z" fill="var(--band-grey)"/>
      <path d="M0 18 Q 170 115 420 80 L420 340 L0 340 Z" fill="var(--paper)"/>
      <path d="M0 24 Q 170 121 420 86 L420 340 L0 340 Z" fill="var(--brand-red)"/>
    </svg>
    <address class="contact">
      <span class="contact__phone">0452 918 304</span>
      <span class="contact__web">brackenridgestrengthstudio.example.com.au</span>
      <span class="contact__address">4/63 Juniper Hollow Rd, Brackenridge</span>
    </address>
  </article>

  <article class="flyer flyer--cover">
    <div class="brand-name">Brackenridge Strength Studio</div>
    <h1 class="headline">
      <span class="headline__lead">Health Through</span>
      <span class="headline__key">Strength</span>
    </h1>
    <div class="photo photo--back" role="img" aria-label="Photo of a man's bare back with hands on his lower back, pain highlighted in red"></div>
    <svg class="base" viewBox="0 0 420 370" preserveAspectRatio="none" aria-hidden="true">
      <path d="M0 0 Q 170 95 420 62 L420 370 L0 370 Z" fill="var(--band-grey)"/>
      <path d="M0 18 Q 170 115 420 80 L420 370 L0 370 Z" fill="var(--paper)"/>
      <path d="M0 24 Q 170 121 420 86 L420 370 L0 370 Z" fill="var(--brand-red)"/>
    </svg>
    <address class="contact">
      <span class="contact__phone">0452 918 304</span>
      <span class="contact__web">brackenridgestrengthstudio.example.com.au</span>
      <span class="contact__address">4/63 Juniper Hollow Rd, Brackenridge</span>
    </address>
  </article>

</body>
</html>
```